Fabrication and machining company needing printed material designs.

Heronfield Vessels, Inc. wants to use appealing visuals as well as informative text to tell potential clients about our capabilities in fabrication and machining. We have a new logo to showcase as well as a new website. The use of print media will allow us to leave tangible information with clients, and therefore the design will need to be concise, informative, and visually appealing.

Full Page Flyer (approx. 8.5" x 11"), front and back design. This will be a detailed offering of capabilities and services for our shop.

Half Page Flyer (approx. 5.5" x 8.5"), front and back design. An abbreviated version of the full page flyer, meant to be easily handed out and stored inside a note book.

Bi-fold business card front and back. General offerings of our services. Minimal if any details. Finished size is twice the size of a business card (approx. 4" x 3.5"), once folded in half will be the same size as a standard business card (approx. 2" x 3.5").

Please use www.heronfieldvesselsinc.example for theme ideas. The font used for our logo is ethnocentric, not to be used for all text.

Target Market(s)

Industrial Consumers

Font styles to use
Sans Serif

```html
<!DOCTYPE html>
<html lang="en">
<head>
<meta charset="utf-8">
<title>Heronfield Vessels, Inc. — Flyer Front and Back</title>
<link rel="stylesheet" href="https://fonts.googleapis.com/css2?family=Orbitron:wght@700;800&family=Lato:ital,wght@0,400;0,700;1,700;1,900&display=swap">
<style>
:root{
  --bg:#e4e6e9;
  --dark:#444547;
  --dark-2:#58595b;
  --dark-3:#636466;
  --blue:#5b95d5;
  --blue-deep:#3f7fcb;
  --orange:#ef8a2a;
  --white:#ffffff;
  --steel:#a9b0b6;
}
*{margin:0;padding:0;box-sizing:border-box}
html,body{width:1200px;height:818px;overflow:hidden;background:var(--bg);font-family:"Lato",Arial,sans-serif}
.page{position:absolute;top:88px;width:498px;height:642px;background:var(--white);overflow:hidden;box-shadow:3px 4px 8px rgba(0,0,0,.25)}
.page--front{left:83px}
.page--back{left:619px}
.abs{position:absolute}
.display{font-family:"Orbitron",Arial,sans-serif;font-weight:800;letter-spacing:.5px}
.brand{position:absolute;color:var(--white);font-family:"Lato",Arial,sans-serif;font-weight:700;display:flex;align-items:center;gap:8px}
.brand__mark{width:14px;height:14px;background:var(--white);flex:none}
.photo{position:absolute}

/* front */
.front__band{left:0;top:0}
.front__title{left:282px;top:30px;color:var(--blue);font-size:21px;line-height:30px}
.front__title small{font-size:11px}
.hero{left:0;top:118px;width:498px;height:232px;background:linear-gradient(90deg,var(--blue) 0%,var(--blue) 40%,#8fa9c4 70%,#b9c2ca 100%)}
.hero__headline{left:26px;top:150px;color:var(--white);font-size:30px;line-height:40px;text-shadow:1px 2px 3px rgba(0,0,0,.35)}
.hero__headline small{font-size:13px}
.hero__rule{left:26px;top:236px;width:240px;height:2px;background:var(--orange)}
.hero__tagline{left:26px;top:244px;color:var(--white);font-style:italic;font-weight:900;font-size:29px;line-height:34px;letter-spacing:-.5px;text-shadow:1px 2px 3px rgba(0,0,0,.35)}
.features{left:11px;top:350px;width:475px;height:213px;display:flex}
.feature{flex:1;padding:10px 6px 0;text-align:center;color:var(--white)}
.feature:nth-child(odd){background:var(--dark-2)}
.feature:nth-child(even){background:var(--dark-3)}
.feature__photo{height:110px;border:2px solid var(--white)}
.feature__title{margin-top:14px;font-size:11.5px;font-weight:400;letter-spacing:.3px}
.feature__rule{width:118px;height:2px;background:var(--orange);margin:4px auto 6px}
.feature__text{font-size:7.4px;line-height:9.8px;padding:0 10px}
.front__line{left:0;top:573px;width:498px;height:3px;background:var(--dark)}
.contact{left:0;top:577px;width:498px;height:65px;display:flex;justify-content:center;align-items:flex-end;padding-bottom:12px;font-size:11.5px}
.contact--front{background:var(--blue);color:var(--white)}
.contact--back{background:var(--dark);color:var(--blue)}
.contact__item{position:relative;padding:0 10px;text-align:center}
.contact__item + .contact__item{border-left:2px solid currentColor}
.contact__icon{position:absolute;left:50%;top:-30px;transform:translateX(-50%)}

/* back */
.back__band{left:0;top:0}
.about{left:0;top:93px;width:498px;height:104px;background:var(--blue)}
.about__title{left:22px;top:106px;color:var(--white);font-size:23px}
.about__rule{left:22px;top:133px;width:200px;height:2px;background:var(--orange)}
.about__text{left:22px;top:142px;width:462px;color:var(--white);font-size:7.6px;line-height:9.7px}
.flag-frame{left:296px;top:19px;width:180px;height:118px;border:2px solid var(--dark)}
.flag-photo{left:292px;top:23px;width:178px;height:112px;background:linear-gradient(180deg,#6f9ad0 0%,#b9c9dc 70%,#7a7466 100%);border:1px solid var(--white)}
.industries{left:0;top:197px;width:498px;height:309px;background:var(--dark)}
.industries__title{left:0;top:218px;width:498px;text-align:center;color:var(--white);font-size:23px}
.industries__rule{left:184px;top:248px;width:130px;height:2px;background:var(--orange)}
.tank-photo{left:138px;top:282px;width:220px;height:110px;background:linear-gradient(180deg,#c9c4b4 0%,#a9a293 70%,#6d6a60 100%);clip-path:polygon(20% 15%,90% 8%,98% 80%,70% 100%,0 92%)}
.hub-name{left:0;top:394px;width:498px;text-align:center;color:var(--white);font-size:14px}
.label{color:var(--white);font-size:10px;line-height:12.5px;text-align:center}
.products{left:0;top:506px;width:498px;height:70px;background:var(--white);border-top:3px solid var(--blue);border-bottom:3px solid var(--blue)}
.products__name{left:0;top:520px;width:230px;text-align:right;color:var(--blue-deep);font-size:16.5px;line-height:21px}
.products__divider{left:240px;top:522px;width:2px;height:40px;background:var(--blue-deep)}
.products__list{left:248px;top:522px;color:var(--blue-deep);font-size:8.6px;line-height:12px}
</style>
</head>
<body>

<!-- FRONT -->
<section class="page page--front">
  <svg class="abs front__band" width="498" height="118" aria-hidden="true">
    <polygon points="0,0 278,0 214,118 0,118" fill="#444547"/>
  </svg>
  <div class="brand" style="left:30px;top:50px;font-size:13px"><span class="brand__mark"></span>HERONFIELD VESSELS INC.</div>
  <h1 class="abs front__title display">HERONFIELD<br>VESSELS <small>INC.</small></h1>

  <div class="abs hero" role="img" aria-label="Photograph of tall grey storage tanks and piping at a production site under a blue sky"></div>
  <h2 class="abs hero__headline display">HERONFIELD<br>VESSELS <small>INC.</small></h2>
  <div class="abs hero__rule"></div>
  <p class="abs hero__tagline">is a leading tank<br>manufacturer.</p>

  <div class="abs features">
    <article class="feature">
      <div class="feature__photo" role="img" aria-label="Photograph of a pump skid with blue and orange motors in the shop" style="background:linear-gradient(135deg,#8a8378,#b5a99a 50%,#5c7fb8)"></div>
      <h3 class="feature__title">WHO WE ARE</h3>
      <div class="feature__rule"></div>
      <p class="feature__text">Our world runs on natural and renewable resources. We are proud to make our livelihood supporting the industries that provide our quality of life.</p>
    </article>
    <article class="feature">
      <div class="feature__photo" role="img" aria-label="Photograph of a crane truck lifting tanks in a yard" style="background:linear-gradient(180deg,#6e9fd8,#a7b4bd 55%,#7a6a52)"></div>
      <h3 class="feature__title">WHY CHOOSE US</h3>
      <div class="feature__rule"></div>
      <p class="feature__text">It all begins with integrity. We pride ourselves in the craftsmanship we send our customers. From concept through delivery we strive for excellence.</p>
    </article>
    <article class="feature">
      <div class="feature__photo" role="img" aria-label="Photograph of a large dark tank loaded on a truck trailer" style="background:linear-gradient(180deg,#7fb0e2,#3d3f44 55%,#6b6a66)"></div>
      <h3 class="feature__title">OUR TEAM</h3>
      <div class="feature__rule"></div>
      <p class="feature__text">We are welders and fabricators, as well as parents, neighbors, and civic volunteers. We take our work ethic and use it to build a better community.</p>
    </article>
  </div>

  <div class="abs front__line"></div>
  <footer class="abs contact contact--front">
    <div class="contact__item"><svg class="contact__icon" width="24" height="24" viewBox="0 0 24 24" fill="none" stroke="currentColor" stroke-width="1.3"><circle cx="12" cy="12" r="11"/><path d="M12 18s-4-4.5-4-7.5a4 4 0 0 1 8 0c0 3-4 7.5-4 7.5z"/><circle cx="12" cy="10.5" r="1.4"/></svg>PO Box 417 Alderway UT 84000</div>
    <div class="contact__item"><svg class="contact__icon" width="24" height="24" viewBox="0 0 24 24" fill="none" stroke="currentColor" stroke-width="1.3"><circle cx="12" cy="12" r="11"/><path d="M6.5 10.5 12 7l5.5 3.5v6h-11z"/><path d="M6.5 10.5 12 14l5.5-3.5"/></svg>office@heronfieldvesselsinc.example</div>
    <div class="contact__item"><svg class="contact__icon" width="24" height="24" viewBox="0 0 24 24" fill="none" stroke="currentColor" stroke-width="1.3"><circle cx="12" cy="12" r="11"/><path d="M8 7h2.5l1 3-1.5 1a6 6 0 0 0 3 3l1-1.5 3 1V16a1 1 0 0 1-1 1A9 9 0 0 1 7 8a1 1 0 0 1 1-1z"/></svg>(555) 014-2698</div>
  </footer>
</section>

<!-- BACK -->
<section class="page page--back">
  <svg class="abs back__band" width="498" height="93" aria-hidden="true">
    <polygon points="0,0 260,0 208,93 0,93" fill="#444547"/>
  </svg>
  <div class="brand" style="left:30px;top:38px;font-size:11px"><span class="brand__mark"></span>HERONFIELD VESSELS INC.</div>

  <div class="abs about"></div>
  <div class="abs flag-frame"></div>
  <div class="abs flag-photo" role="img" aria-label="Photograph of a large national flag suspended between two crane booms over a street"></div>
  <h2 class="abs about__title display">ABOUT US</h2>
  <div class="abs about__rule"></div>
  <p class="abs about__text">Heronfield Vessels Inc. is a leading tank manufacturer located in Rocky Mountain region. We specialize in API-12F &amp; API-650 tank manufacturing serving Utah, Colorado, Wyoming, and North Dakota. We started with tanks and tank accessories in 2006, since then we have added cone bottom and mixer tanks, pump skids, clarifiers arms, wind turbine transport components, and custom fabrication &amp; metal forming to meet our customers needs. Most recently, we have added machining services and stainless steel fabrication in a separate facility.</p>

  <div class="abs industries"></div>
  <h2 class="abs industries__title display">INDUSTRIES SERVED</h2>
  <div class="abs industries__rule"></div>
  <div class="abs tank-photo" role="img" aria-label="Photograph of a row of beige storage tanks with a catwalk"></div>
  <div class="abs hub-name display">HERONFIELD VESSELS</div>

  <svg class="abs" style="left:0;top:197px" width="498" height="309" aria-hidden="true">
    <path d="M96 79 C 100 230, 170 277, 246 277 C 322 277, 398 230, 402 79" fill="none" stroke="#fff" stroke-width="2.2" stroke-dasharray="0 8" stroke-linecap="round"/>
    <g fill="#ef8a2a" stroke="#fff" stroke-width="3">
      <circle cx="96" cy="79" r="7"/><circle cx="124" cy="217" r="7"/><circle cx="246" cy="277" r="7"/><circle cx="373" cy="217" r="7"/><circle cx="402" cy="79" r="7"/>
    </g>
    <g fill="none" stroke="#fff" stroke-width="1.4">
      <circle cx="58" cy="81" r="20"/><circle cx="78" cy="215" r="20"/><circle cx="248" cy="241" r="20"/><circle cx="441" cy="213" r="20"/><circle cx="441" cy="81" r="20"/>
    </g>
    <g fill="#fff">
      <path d="M50 92h16v2H50zM57 92l1-14h2l1 14zM48 76l18-4 .5 2-18 4z"/>
      <path d="M71 216h14v3H71zM76 210h4v6h-4zM73 207h10v3H73zM77 221h2v4h-2z"/>
      <path d="M240 234l14 14-1.5 1.5-14-14zM238 240a12 8 0 0 1 12-8l-1 2a10 6 0 0 0-9 7z"/>
      <path d="M432 222l12-14 2 1.5-12 14zM436 222h14v2h-14z"/>
      <path d="M440 72h2v20h-2zM441 80l-8 5-1-1.5 8-5zM441 80l8 5 1-1.5-8-5zM441 80v-9h-.5v9z"/>
    </g>
  </svg>
  <div class="abs label" style="left:38px;top:294px;width:40px">Oil &amp;<br>Gas</div>
  <div class="abs label" style="left:44px;top:458px;width:80px;text-align:left">Water &amp; Waste<br>Water</div>
  <div class="abs label" style="left:218px;top:578px;width:60px">MINING</div>
  <div class="abs label" style="left:464px;top:308px;width:0"></div>
  <div class="abs label" style="left:410px;top:458px;width:60px">Aggregate</div>
  <div class="abs label" style="left:412px;top:292px;width:74px">Power<br>Generation</div>

  <div class="abs products"></div>
  <p class="abs products__name">OIL PRODUCTION<br>TANKS &amp; ACCESSORIES</p>
  <div class="abs products__divider"></div>
  <ul class="abs products__list" style="list-style:none">
    <li>• API 12-F, API 650 SPECIFICATION BUILT TANKS</li>
    <li>• FIRE TUBES/TANK HEATERS</li>
    <li>• TANK COILS • WALKWAYS • STAIRS</li>
  </ul>

  <footer class="abs contact contact--back">
    <div class="contact__item"><svg class="contact__icon" width="24" height="24" viewBox="0 0 24 24" fill="none" stroke="currentColor" stroke-width="1.3"><circle cx="12" cy="12" r="11"/><path d="M12 18s-4-4.5-4-7.5a4 4 0 0 1 8 0c0 3-4 7.5-4 7.5z"/><circle cx="12" cy="10.5" r="1.4"/></svg>PO Box 417 Alderway UT 84000</div>
    <div class="contact__item"><svg class="contact__icon" width="24" height="24" viewBox="0 0 24 24" fill="none" stroke="currentColor" stroke-width="1.3"><circle cx="12" cy="12" r="11"/><path d="M6.5 10.5 12 7l5.5 3.5v6h-11z"/><path d="M6.5 10.5 12 14l5.5-3.5"/></svg>office@heronfieldvesselsinc.example</div>
    <div class="contact__item"><svg class="contact__icon" width="24" height="24" viewBox="0 0 24 24" fill="none" stroke="currentColor" stroke-width="1.3"><circle cx="12" cy="12" r="11"/><path d="M8 7h2.5l1 3-1.5 1a6 6 0 0 0 3 3l1-1.5 3 1V16a1 1 0 0 1-1 1A9 9 0 0 1 7 8a1 1 0 0 1 1-1z"/></svg>(555) 014-2698</div>
  </footer>
</section>

</body>
</html>
```